Dentistry Office

We want a new design for a Dentist's office website.

The theme is: "We provide high quality, state-of-the-art, dental care in a comfortable, caring environment."

The site currently has a menu on the left of the page with about 40 items on it. There is a great deal of textual content on each page, plus several illustrations.

We want to do this using CSS, so we need specifications in the CSS for all possible elements. The CSS needs to be named in a logical manner for easy use.

Every dentist on the planet seems to use lots of Flash. We don't want to because it is so distracting. We are looking for an elegant solution targeting 24-55 age group, but not excluding anyone.

The following (from another dentist's site) can give you a taste of what we want to communicate on the site:

"After 20 years of teaching dentists how to refine their technique and many years of writing textbooks, I currently devote my time to my office and the hands-on practice of dentistry. I'd like to welcome you personally to my dental practice, and I invite you to meet my highly experienced team of professionals.

"We have offered complete dental care of the highest quality since 1978. We provide Preventive Services, Tooth Whitening and Cosmetic Dentistry for a beautiful smile, Endodontics (root canal treatment) to treat painful teeth, Sedation Dentistry so you can relax, and Dental Implants to restore what is missing. We offer total care.

"Our approach to your health is simple: We use our education, experience and dedication to provide every patient with superior dental care.

"This passion for excellence is not just a goal, but a standard every member of our team holds.

"We also pride ourselves with our state of the art procedures, training and technology. This includes creating a beautiful smile using techniques that preserve as much of the original tooth as possible.

"Our abilities are renowned throughout the dental profession and I hope if you have any questions you will contact us by an e-mail note, by phone or just by dropping by."

Keep in mind the screen shape and dimensions. Your design needs to work in the normal screen proportions, regardless of how it looks when you post it here. Scrolling is OK, but the first impression needs to work.

Keep in mind that there will be about 250 words, or more, on each page.

Competitors web sites:

http://www.brellwickdentist.example/

http://www.brellwickdentalcare.example/

http://www.grinsbybrellwickdental.example/

http://www.dorvanfamilydentalcare.example/

http://www.brellwickdental.example/

http://www.quimbertdental.example/

We need to compete with these.

Target Market(s)

Generally adults seeking the most experienced and comfortable-to-be-with dentist.

Industry/Entity Type

Training

Requirements
Must have
• Must stand apart from other dentists.
• Must be elegant.
• Must have a horizontal menu structure across all columns, NOT a vertical that requires scrolling, no popout, pop down, etc. menus.
• We are looking for something special.
• Do not waste your time or ours putting up templates and things you have used before.
• Personally, I do not see how someone outside the US can understand the northern California dental market. But you are welcome to try.
Should not have
• Flash or graphics that move
• The look of a template
• Folksy fonts
• Looks like you used it 20 times before

```html
<!DOCTYPE html>
<html lang="en">
<head>
<meta charset="utf-8">
<title>Owen Calder, DDS, FAGD – Brellwick Dentist</title>
<link rel="stylesheet" href="https://fonts.googleapis.com/css2?family=Arimo:wght@400;700&family=Tinos:wght@400;700&display=swap">
<style>
:root{
  --ink:#333a44;
  --muted:#5c6570;
  --navy:#23466f;
  --link:#2f6aa6;
  --nav:#3b4756;
  --nav-line:#56657a;
  --sky:#87aed2;
  --sky-deep:#5f8dbb;
  --bar:#dde5ee;
  --bar-line:#c4d0dc;
  --panel:#f3f6f9;
  --footer:#d9dde2;
  --white:#ffffff;
}
*{box-sizing:border-box;margin:0;padding:0}
html,body{width:1200px;height:2516px;overflow:hidden;background:var(--white)}
body{font-family:"Arimo",Arial,sans-serif;color:var(--ink);font-size:14px;line-height:1.5;position:relative}
a{color:var(--link)}
.site-header{position:relative;height:160px}
.practice-name{position:absolute;left:22px;top:12px;font-family:"Tinos",Georgia,serif;font-weight:700;font-size:30px;color:var(--navy);line-height:1.1}
.practice-tag{position:absolute;left:24px;top:52px;font-family:"Tinos",Georgia,serif;font-size:17px;color:var(--muted)}
.address{position:absolute;left:720px;top:14px;font-size:12px;line-height:1.5;color:var(--muted)}
.hero-photo{position:absolute;right:0;top:0;width:330px;height:440px;background:linear-gradient(160deg,#e9eef3 0%,#c9d6e4 45%,#9ab6d3 100%);z-index:1}
.main-nav{position:absolute;left:0;top:128px;width:1200px;height:32px;background:var(--nav);display:flex;z-index:2}
.main-nav a{color:var(--white);text-decoration:none;font-weight:700;font-size:13px;padding:0 26px;line-height:32px;border-right:1px solid var(--nav-line)}
.hero{height:280px;background:linear-gradient(90deg,var(--sky-deep),var(--sky) 70%);position:relative}
.hero-lead{position:absolute;left:40px;top:40px;width:560px;color:var(--white);font-family:"Tinos",Georgia,serif;font-size:24px;line-height:1.3;font-weight:700}
.topic-menu{display:flex;height:236px;background:var(--panel);border-bottom:1px solid var(--bar-line);padding:14px 20px 16px}
.topic{flex:1;padding-right:14px}
.topic h3{font-size:14px;color:var(--navy);margin-bottom:6px;line-height:1.3}
.topic ul{margin:0}
.topic li{list-style:none;font-size:11px;line-height:16px}
.topic li::before{content:"› ";color:var(--sky-deep)}
.body-wrap{display:flex;padding:20px 20px 0}
.content{width:880px}
.sidebar{width:260px;margin-left:20px;padding-top:300px}
h1.welcome{font-size:22px;color:var(--navy);margin-bottom:10px}
.intro p{margin-bottom:8px}
h2.challenges{font-size:16px;color:var(--navy);margin:14px 0 8px}
.topic-box{border:1px solid var(--bar-line);margin-bottom:12px}
.topic-box h2{background:var(--bar);font-size:16px;color:var(--navy);padding:5px 10px;border-bottom:1px solid var(--bar-line)}
.box-body{display:flex;gap:16px;padding:10px}
.box-body p{margin-bottom:7px}
.box-text{flex:1}
.box-photo{width:140px;height:110px;flex:none;background:linear-gradient(135deg,#d7dfe8,#a9bccf)}
.smile-pair{display:flex;gap:10px;justify-content:center;margin:8px 0}
.smile-pair div{width:150px;height:100px;background:linear-gradient(135deg,#f1e6da,#cdb8a2)}
.twin{display:flex;gap:14px}
.twin .topic-box{flex:1}
.strong{font-weight:700}
.map-title{font-weight:700;color:var(--navy);font-size:14px;margin-bottom:6px}
.map{width:260px;height:330px;background:linear-gradient(160deg,#eef1e8,#d6e0d0);border:1px solid var(--bar-line)}
.map-link{display:block;text-align:right;font-size:11px;margin-top:4px}
.hours{margin-top:30px;text-align:center}
.hours h3{font-family:"Tinos",Georgia,serif;font-size:20px;color:var(--navy);margin-bottom:4px}
.hours p{font-size:12px;margin-bottom:6px}
.hours li{list-style:none;font-size:13px;line-height:1.7}
.site-footer{position:absolute;left:0;top:2380px;width:1200px;height:136px;background:var(--footer);padding:18px 24px;display:flex;justify-content:space-between;font-size:12px;line-height:1.45}
.footer-links h4{font-size:12px;margin-bottom:8px}
.badges{display:flex;gap:14px}
.badge{width:110px;height:60px;background:var(--white);border:1px solid var(--bar-line)}
</style>
</head>
<body>
<header class="site-header">
  <div class="practice-name">Owen Calder, DDS, FAGD</div>
  <div class="practice-tag">Brellwick Dentist</div>
  <div class="address">Owen Calder, DDS<br>418 Larkmoor Rd, Ste C<br>Brellwick, CA 95099<br>(555) 575-0142</div>
  <div class="hero-photo" role="img" aria-label="Smiling patient portrait"></div>
  <nav class="main-nav">
    <a href="#">Home</a><a href="#">Why Are We Different?</a><a href="#">Technologies We Offer</a><a href="#">Meet Dr. Calder</a><a href="#">Our Staff</a><a href="#">Contact Us / Links</a>
  </nav>
</header>
<section class="hero">
  <p class="hero-lead">Brellwick Dentist - Owen Calder, DDS, Providing Cosmetic Dentistry Excellence to Patients in Brellwick, Sonoma County and the San Francisco Bay Area.</p>
</section>
<nav class="topic-menu">
  <div class="topic"><h3>Education</h3><ul><li>Emergency Dental Care</li><li>Your Mouth</li><li>Your Teeth</li><li>Cracked Teeth</li><li>Wisdom Teeth</li><li>Dentures &amp; Partials</li><li>Dry Mouth</li><li>Tooth Grinding</li><li>Sleep Dentistry</li><li>Videos</li></ul></div>
  <div class="topic"><h3>Preventive</h3><ul><li>What is Preventive Care?</li><li>Taking Care of Your Teeth</li><li>Baby Teeth</li><li>Dental Check-ups</li><li>Sealants</li><li>Periodontal Disease</li><li>Halting the Habit</li><li>Night Guards</li><li>Dental X-Rays</li><li>Antibiotics with Treatment</li></ul></div>
  <div class="topic"><h3>Cosmetics</h3><ul><li>Cosmetic Dentistry</li><li>Reshaping and Whitening</li><li>Cosmetic Bonding</li><li>Esthetic Veneers</li><li>Tooth Shaping</li></ul></div>
  <div class="topic"><h3>Restorations</h3><ul><li>Crowns/Caps: Each Step</li><li>Same-Day Crowns</li><li>Porcelain Bridges</li><li>Bonded Dental Bridges</li><li>Gold Restorations</li><li>Implants</li><li>Treating Cracked Teeth</li><li>Periodontal Splint Treatment</li></ul></div>
  <div class="topic"><h3>Visiting our office</h3><ul><li>Where to Stay</li><li>First Visit Map</li><li>Financial Policy</li><li>Dental Insurance</li></ul></div>
</nav>
<div class="body-wrap">
  <main class="content">
    <h1 class="welcome">Welcome to Our Website</h1>
    <div class="intro">
      <p>In Brellwick, when you're a patient of Dr. Calder, you can be confident that you're receiving care from the most experienced, knowledgeable, and skilled cosmetic dentist in Sonoma County.</p>
      <p>Dr. Calder is an award-winning leader in restorative dentistry and a professional. His humor, dedication, and talent ensure you a pleasant experience and superb, long-lasting results.</p>
    </div>
    <h2 class="challenges">What Are Your Dental Challenges?</h2>
    <section class="topic-box"><h2>Toothaches?</h2><div class="box-body"><div class="box-text">
      <p>Toothaches are about as bad a pain as you can experience. We know and we sympathize. That's why we make every effort to bring you immediate relief by keeping room in our schedule for this type of emergency.</p>
      <p>Give us a call right now at (555) 575-0142 and we'll get you in TODAY.</p>
      <p class="strong">Toothaches can largely be avoided with proper preventive care.</p>
    </div><div class="box-photo" role="img" aria-label="Patient holding jaw in pain"></div></div></section>
    <section class="topic-box"><h2>Dental Check-Ups</h2><div class="box-body"><div class="box-text">
      <p>Dental check-ups and removal of plaque and tartar from your teeth are the cornerstones of good dental health. Not only can you prevent most toothaches, you may be surprised at how much better and more beautiful your entire smile looks. Low-grade infections may be lurking in your gums and sapping your energy. See more information by visiting our pages under Preventative in the left side bar.</p>
      <p>Dental check-ups should become a routine habit and be done at least every six months. You will also save a lot of money by avoiding big repair bills later on.</p>
      <p>Give us a call right now at (555) 575-0142 and make an appointment!</p>
    </div><div class="box-photo" role="img" aria-label="Hygienist cleaning a patient's teeth"></div></div></section>
    <section class="topic-box"><h2>Deathly Fear of Dentist?</h2><div class="box-body"><div class="box-text">
      <p>With today's technologies there is no longer an excuse. You can be blissfully asleep while even major procedures are performed. When you wake up, everything is done and you're on your way. We specialize in sedation dentistry, also known as sleep dentistry. If you have a fear of dentists, let us show you how comfortable a visit can truly be.</p>
      <p>Give us a call right now at (555) 575-0142 and make an appointment.</p>
    </div><div class="box-photo" role="img" aria-label="Relaxed patient resting in dental chair"></div></div></section>
    <section class="topic-box"><h2>Cosmetic Dentistry</h2><div class="box-body"><div class="box-text">
      <p class="strong">Who do you think will get the date or have the winning job interview?</p>
      <p>When face-to-face with an important person, nothing speaks louder than a winning smile. Crooked teeth, gaps in your teeth or stains are NOT part of a winning smile. Learn more about our cosmetic dentistry services by clicking on the pages under Cosmetics in the left sidebar.</p>
      <div class="smile-pair"><div role="img" aria-label="Smile before treatment"></div><div role="img" aria-label="Smile after treatment"></div></div>
      <p class="strong">Are you ready to crack the code in your favor?</p>
      <p>Give us a call right now at (555) 575-0142 and make an appointment!</p>
    </div></div></section>
    <section class="topic-box"><h2>Concerned about Mercury Amalgams and Radiation Exposure?</h2><div class="box-body"><div class="box-text">
      <p>You are wise to take your health into your own hands and question the things that have been accepted by patients without question in the past. Amalgams, the so-called silver fillings, are a technology that is over 100 years old. It may simply not be the best choice today. Because of the mercury content, we no longer use this technique.</p>
    </div></div></section>
    <section class="topic-box"><h2>Removal of Silver Fillings</h2><div class="box-body"><div class="box-text">
      <p>Many of our patients take preventive action and have their old amalgam fillings removed and replaced with modern materials. We have great care when removing the old material so that the toxic mercury contained in amalgams does not come into contact with the inside of your mouth.</p>
    </div></div></section>
    <div class="twin">
      <section class="topic-box"><h2>Radiation-Free Diagnostics</h2><div class="box-body"><div class="box-text">
        <p>X-ray free decay diagnostics does exist, and we offer this latest technology. It's called Digital Transillumination. Ultra-low-dose radiography for rarer cases is also available. Click here to learn more about all of the latest technologies available at this office.</p>
        <p>If you are a health-conscious patient, give us a call right now at (555) 575-0142 and make an appointment!</p>
      </div></div></section>
      <section class="topic-box"><h2>Free Dental Consultations</h2><div class="box-body"><div class="box-text">
        <p>Let us take a look at your dental challenges, and we will prepare a treatment plan at no cost or obligation to you.</p>
        <p class="strong">Give us a call right now at (555) 575-0142 and make an appointment for a free dental consultation!</p>
      </div></div></section>
    </div>
  </main>
  <aside class="sidebar">
    <div class="map-title">Brellwick Map:</div>
    <div class="map" role="img" aria-label="Street map to the office"></div>
    <a class="map-link" href="#">Click for Larger Map</a>
    <div class="hours">
      <h3>Office Timing</h3>
      <p>Our usual office hours are:</p>
      <ul><li>Monday 9 am to 6 pm</li><li>Tuesday 8 am to 5 pm</li><li>Wednesday 8 am to 5 pm</li><li>Thursday 8 am to 5 pm</li><li>Friday 7:30 am to 3 pm</li></ul>
    </div>
  </aside>
</div>
<footer class="site-footer">
  <div>
    <p>Copyright © 2010 drcalder.example. All Rights Reserved.</p>
    <p style="margin-top:10px">Office Phone: (555) 575-0142<br>418 Larkmoor Rd, Ste C<br>Brellwick, CA 95099<br>Email Dr. Calder: office@drcalder.example</p>
  </div>
  <div class="footer-links">
    <h4>Dental Links:</h4>
    <div class="badges"><div class="badge" role="img" aria-label="Professional association badge"></div><div class="badge" role="img" aria-label="Academy membership badge"></div><div class="badge" role="img" aria-label="Regional society badge"></div></div>
  </div>
</footer>
</body>
</html>
```